Dale Morrikan Plumbing and Heating

Need a card design for a plumbing and heating company that does service and repair, remodels, and plumbing in new construction. Please add following on back side of card; Boilers, Water heaters, Gas lines, Sump pumps, Toilet repairs, Faucet repairs, Pipe thawing, Radiant heating, New construction, Remodels.

Industry/Entity Type

Plumber

Contact Information for Business Card

Was thinking white gloss card with colored logo in middle or black glossy card with silver logo in middle. Just a thought but very open to other designs.

Requirements
Must have
• Need following on front of card;
• P(203) 321-8689
• C(203) 232-9069
• Dale Morrikan 275 Larkwell St West, Stamford, Ct 06214
• service@DrainHearth.example (plumbing in blue, heating in red)
• www.DrainHearth.example (plumbing in blue, heating in red)
• Fully Licensed and Insured
Nice to have
• Elegant design

```html
<!DOCTYPE html>
<html lang="en">
<head>
<meta charset="utf-8">
<title>Dale Morrikan Plumbing and Heating — Business Card</title>
<link rel="stylesheet" href="https://fonts.googleapis.com/css2?family=Open+Sans:wght@400;600&display=swap">
<style>
  :root {
    --page: #e9e7e4;
    --card: #ffffff;
    --ink: #1d1d1f;
    --red: #c9313d;
    --red-dark: #a8242f;
    --blue: #2a4fc4;
    --logo-blue: #3f7fd0;
    --faint: #e4e9f1;
    --faint-2: #f4f6f9;
  }
  * { box-sizing: border-box; margin: 0; padding: 0; }
  html, body { width: 1200px; height: 892px; overflow: hidden; }
  body {
    background: var(--page);
    font-family: "Open Sans", Arial, sans-serif;
    color: var(--ink);
    position: relative;
  }
  .card {
    position: absolute;
    left: 250px;
    width: 700px;
    height: 400px;
    background: var(--card);
    box-shadow: 0 6px 18px rgba(0,0,0,0.18);
    overflow: hidden;
  }
  .card--front { top: 30px; }
  .card--back { top: 462px; }

  /* Front */
  .brand {
    position: absolute;
    left: 34px;
    top: 180px;
    display: flex;
    align-items: center;
    gap: 12px;
  }
  .brand__dot {
    width: 44px; height: 44px;
    border-radius: 50%;
    background: var(--logo-blue);
    flex: none;
  }
  .brand__name {
    font-weight: 600;
    font-size: 17px;
    line-height: 1.25;
    color: var(--logo-blue);
    letter-spacing: 0.4px;
    text-transform: uppercase;
    white-space: nowrap;
  }
  .divider {
    position: absolute;
    left: 318px; top: 60px;
    width: 36px; height: 250px;
  }
  .tagline {
    position: absolute;
    left: 368px; top: 58px;
    font-size: 23px;
    color: var(--red);
    white-space: nowrap;
  }
  .contacts {
    position: absolute;
    left: 372px; top: 150px;
    list-style: none;
  }
  .contacts li {
    display: flex;
    align-items: center;
    gap: 12px;
    font-size: 18px;
    line-height: 31px;
    white-space: nowrap;
  }
  .icon {
    width: 18px; height: 18px;
    background: var(--ink);
    flex: none;
  }
  .blue { color: var(--blue); }
  .red { color: var(--red); }
  .address-band {
    position: absolute;
    left: 0; right: 0; bottom: 0;
    height: 64px;
    background: linear-gradient(var(--red), var(--red-dark));
    color: #fff;
    display: flex;
    align-items: center;
    padding-left: 40px;
    gap: 14px;
    font-size: 23px;
    white-space: nowrap;
  }
  .address-band .icon { background: #fff; }

  /* Back */
  .illustration {
    position: absolute;
    left: 40px; top: 40px;
    width: 300px; height: 320px;
    background: radial-gradient(ellipse at 50% 45%, var(--faint) 0%, var(--faint-2) 60%, rgba(255,255,255,0) 75%);
  }
  .service-rule {
    position: absolute;
    left: 40px; right: 24px; top: 90px;
    height: 1px;
    background: var(--ink);
  }
  .service-end {
    position: absolute;
    right: 24px; top: 90px;
    width: 1px; height: 300px;
    background: var(--ink);
  }
  .service-title {
    position: absolute;
    left: 250px; top: 64px;
    padding: 0 16px;
    background: var(--card);
    font-size: 44px;
    font-weight: 400;
    color: var(--red);
    line-height: 52px;
  }
  .service-list {
    position: absolute;
    left: 140px; top: 160px;
    list-style: none;
    display: grid;
    grid-template-rows: repeat(5, 36px);
    grid-auto-flow: column;
    column-gap: 60px;
  }
  .service-list li {
    display: flex;
    align-items: center;
    gap: 14px;
    font-size: 21px;
    line-height: 36px;
    white-space: nowrap;
  }
  .tick { width: 16px; height: 16px; flex: none; }
</style>
</head>
<body>

<section class="card card--front" aria-label="Card front">
  <div class="brand">
    <span class="brand__dot"></span>
    <p class="brand__name">Dale Morrikan<br>Plumbing and Heating</p>
  </div>

  <svg class="divider" viewBox="0 0 36 250" aria-hidden="true">
    <polygon points="0,0 3,0 36,250 31,250" fill="#1d1d1f"/>
  </svg>

  <p class="tagline">Fully Licensed and Insured</p>

  <ul class="contacts">
    <li>
      <svg class="icon" viewBox="0 0 18 18" aria-hidden="true"><rect width="18" height="18" fill="#1d1d1f"/><path d="M5 4c1 3 4 7 9 9l-1.5 1.5C8 13 5 9 3.5 5.5Z" fill="#fff"/></svg>
      (203) 555-0147
    </li>
    <li>
      <svg class="icon" viewBox="0 0 18 18" aria-hidden="true"><rect width="18" height="18" fill="#1d1d1f"/><rect x="6" y="3" width="6" height="12" rx="1" fill="#fff"/></svg>
      (203) 555-0183
    </li>
    <li>
      <svg class="icon" viewBox="0 0 18 18" aria-hidden="true"><rect width="18" height="18" fill="#1d1d1f"/><circle cx="9" cy="9" r="5" fill="none" stroke="#fff" stroke-width="1.5"/><line x1="4" y1="9" x2="14" y2="9" stroke="#fff"/></svg>
      <span>www.<span class="blue">Drain</span><span class="red">Hearth</span>.example</span>
    </li>
    <li>
      <svg class="icon" viewBox="0 0 18 18" aria-hidden="true"><rect width="18" height="18" fill="#1d1d1f"/><rect x="3" y="5" width="12" height="8" fill="none" stroke="#fff" stroke-width="1.3"/><path d="M3 5l6 5 6-5" fill="none" stroke="#fff" stroke-width="1.3"/></svg>
      <span>service@<span class="blue">Drain</span><span class="red">Hearth</span>.example</span>
    </li>
  </ul>

  <div class="address-band">
    <svg class="icon" viewBox="0 0 18 18" aria-hidden="true"><rect width="18" height="18" fill="#fff"/><path d="M9 3l6 6h-2v6H5V9H3z" fill="#c9313d"/></svg>
    Dale Morrikan 275 Larkwell St West, Stamford, Ct 06214
  </div>
</section>

<section class="card card--back" aria-label="Card back">
  <div class="illustration" role="img" aria-label="Faint illustration of a plumbing pipe and faucet"></div>
  <div class="service-rule"></div>
  <div class="service-end"></div>
  <h2 class="service-title">Service :</h2>
  <ul class="service-list">
    <li><svg class="tick" viewBox="0 0 16 16" aria-hidden="true"><path d="M2 9l4 4 8-11" fill="none" stroke="#2a4fc4" stroke-width="3"/></svg>Boilers</li>
    <li><svg class="tick" viewBox="0 0 16 16" aria-hidden="true"><path d="M2 9l4 4 8-11" fill="none" stroke="#2a4fc4" stroke-width="3"/></svg>Water heaters</li>
    <li><svg class="tick" viewBox="0 0 16 16" aria-hidden="true"><path d="M2 9l4 4 8-11" fill="none" stroke="#2a4fc4" stroke-width="3"/></svg>Gas lines</li>
    <li><svg class="tick" viewBox="0 0 16 16" aria-hidden="true"><path d="M2 9l4 4 8-11" fill="none" stroke="#2a4fc4" stroke-width="3"/></svg>Sump pumps</li>
    <li><svg class="tick" viewBox="0 0 16 16" aria-hidden="true"><path d="M2 9l4 4 8-11" fill="none" stroke="#2a4fc4" stroke-width="3"/></svg>Toilet repairs</li>
    <li><svg class="tick" viewBox="0 0 16 16" aria-hidden="true"><path d="M2 9l4 4 8-11" fill="none" stroke="#2a4fc4" stroke-width="3"/></svg>Remodels</li>
    <li><svg class="tick" viewBox="0 0 16 16" aria-hidden="true"><path d="M2 9l4 4 8-11" fill="none" stroke="#2a4fc4" stroke-width="3"/></svg>Pipe thawing</li>
    <li><svg class="tick" viewBox="0 0 16 16" aria-hidden="true"><path d="M2 9l4 4 8-11" fill="none" stroke="#2a4fc4" stroke-width="3"/></svg>Faucet repairs</li>
    <li><svg class="tick" viewBox="0 0 16 16" aria-hidden="true"><path d="M2 9l4 4 8-11" fill="none" stroke="#2a4fc4" stroke-width="3"/></svg>Radiant heating</li>
    <li><svg class="tick" viewBox="0 0 16 16" aria-hidden="true"><path d="M2 9l4 4 8-11" fill="none" stroke="#2a4fc4" stroke-width="3"/></svg>New construction</li>
  </ul>
</section>

</body>
</html>
```